Technology management company looking for a new website with a professional look

Brennick IT is a recently re-branded technology management company that is looking for a website design to match its personalized approach and friendly culture.

We would like to see a specialized, but related, page style for each of our main service offerings of:

• Commercial IT Support (This is our primary focus)
• Commercial Phone Systems (We partner with http://www.voxtrell.com/ for our phone systems)
• Point of Sale Systems (We partner with http://www.tillmora.com/ for our POS systems.
• Web Design
• Hollow Pine Computers (Our residential computer service offering, branded as Hollow Pine Computers)

The Hollow Pine Computers page should be build upon the Hollow Pine Computers logo, the other four pages should be branded as Brennick IT.

These five separate pages should have subtle, yet clearly defined links to one another. They should also each have a Home, Products, Service, and Company in the menu.

The website should have a clean design with professional appeal, but not appear too sterile or uninviting. It needs to have a simple, easy to navigate menu interface along the top. We would also like the site to be mobile friendly.

It should also allow us to easily tie in links to our social media pages (Facebook, LinkedIn, Twitter and Google+) and provide easy access to our contact information from each page.

This is a link to our old website www.hollowpinecomputers.com

We don't currently have copy available. The text and menu design should be easily editable and expandable so we can use the design to fit our copy.

In general we are looking for a concept we can modify to fit our needs.

We need this design to be available with layers in a .psd format.

Target Market(s)

Small to mid-size businesses.

Industry/Entity Type

Information Technology

Number of Pages Required

5+ page

Font styles to use
Sans Serif

Requirements
Must have
• Mobile Friendly
• Professional Type Face
• Unity between all pages
• .PSD Format
Nice to have
• Themed with our logo
Should not have
• Bubbly unprofessional typeface. No comic sans.

```html
<!DOCTYPE html>
<html lang="en">
<head>
<meta charset="utf-8">
<title>Hollow Pine Computers</title>
<link href="https://fonts.googleapis.com/css2?family=Open+Sans:wght@400;600;700;800&display=swap" rel="stylesheet">
<style>
:root{
  --navy:#0d2a4a;
  --navy-deep:#0a2240;
  --blue:#1f6fb5;
  --blue-bright:#2a8ad8;
  --sky:#4fb4e8;
  --band:#e6eef3;
  --ink:#27313b;
  --muted:#7b8690;
  --white:#ffffff;
  --footer:#0b1f36;
  --bottom:#07172a;
}
*{box-sizing:border-box;margin:0;padding:0}
html,body{width:670px;height:1200px;overflow:hidden}
body{font-family:"Open Sans",Arial,sans-serif;color:var(--ink);background:var(--white);font-size:8px;line-height:1.45}
a{color:inherit;text-decoration:none}

/* header */
.site-header{height:34px;display:flex;align-items:center;justify-content:space-between;padding:0 38px;background:var(--white)}
.brand{display:flex;align-items:center;gap:6px;font-weight:800;font-size:11px;color:var(--navy);text-transform:uppercase;letter-spacing:.3px}
.brand-mark{width:16px;height:16px;border-radius:50%;background:var(--blue)}
.main-nav{display:flex;gap:20px;font-size:7.5px;font-weight:600;color:#55606a;letter-spacing:.4px}
.main-nav .login{color:var(--blue)}

/* hero */
.hero{height:268px;background:radial-gradient(ellipse at 55% 45%,#3a8fd0 0%,#1a4f86 28%,#0c2c55 60%,#06152b 100%);display:flex;flex-direction:column;align-items:center;justify-content:flex-end;padding-bottom:46px;color:var(--white);text-align:center}
.hero h1{font-size:33px;font-weight:700;letter-spacing:1px;line-height:1.05}
.hero p{font-size:18px;font-weight:600;letter-spacing:.5px;margin-top:4px}

/* welcome */
.welcome{height:142px;display:flex;gap:26px;padding:22px 38px 0}
.welcome-text{flex:1}
.welcome h2{font-size:10.5px;font-weight:700;color:var(--navy);text-transform:uppercase;margin-bottom:4px}
.rule{width:26px;height:2px;background:var(--blue);margin-bottom:10px}
.welcome p{font-size:6.8px;color:var(--muted);margin-bottom:7px}
.storefront{width:190px;height:96px;background:linear-gradient(180deg,#d7dde2 0%,#b9c3cc 45%,#9a3a3a 46%,#c65555 60%,#e9ecef 61%,#cfd6dc 100%)}

/* services */
.services{height:182px;background:var(--band);display:flex;justify-content:space-between;align-items:flex-start;padding:40px 38px 0}
.service{width:104px;text-align:center}
.service svg{width:24px;height:24px;margin-bottom:8px}
.service h3{font-size:6.8px;font-weight:700;color:var(--navy);text-transform:uppercase;line-height:1.3;margin-bottom:5px}
.service p{font-size:6.3px;color:var(--muted)}
.service .more{display:block;font-size:6.3px;color:var(--blue);margin-top:4px}

/* partners */
.partners-block{height:174px}
.partners{padding:20px 38px 0;display:flex;gap:30px}
.partners section{flex:1}
.partners h2{font-size:8.5px;font-weight:700;color:var(--navy);text-transform:uppercase;margin-bottom:4px}
.logo-row{display:flex;align-items:center;justify-content:space-between;height:42px;margin-top:14px}
.partner-name{font-size:12px;font-weight:700;color:#6c7680}
.partner-sq{width:18px;height:18px;background:#8a939b}
.certs{display:flex;justify-content:center;gap:46px;padding:22px 0 0}
.cert{width:74px;height:20px;background:#cdd4da}

/* blog & quotes */
.stories{height:204px;background:linear-gradient(180deg,var(--navy) 0%,var(--navy-deep) 100%);color:var(--white);display:flex;gap:30px;padding:20px 38px 0}
.stories section{flex:1}
.badge{width:22px;height:22px;border-radius:50%;border:1.5px solid var(--sky);display:flex;align-items:center;justify-content:center;margin-bottom:10px}
.stories h2{font-size:9.5px;font-weight:700;text-transform:uppercase;margin-bottom:4px}
.stories h3{font-size:7.5px;font-weight:600;margin-bottom:2px}
.stories .meta{font-size:6px;color:#8fb0cf;margin-bottom:6px}
.stories p{font-size:6.3px;color:#c3d2e0;margin-bottom:6px}
.stories .more{font-size:6.3px;color:var(--sky)}
.quote{font-style:italic}
.author{text-align:right;font-size:7px;font-weight:700;margin-top:8px}

/* contact strip */
.contact-strip{background:var(--blue);color:var(--white);display:flex;align-items:center;justify-content:space-between;padding:0 38px;height:58px}
.contact-strip h2{font-size:11px;font-weight:700;line-height:1.1;text-transform:uppercase}
.cta{display:flex;align-items:center;gap:7px;font-size:6.5px;text-transform:uppercase;font-weight:600;line-height:1.25}
.cta strong{display:block;font-size:7.5px}
.cta-icon{width:20px;height:20px;border-radius:50%;border:1.5px solid var(--white);display:flex;align-items:center;justify-content:center}

/* footer */
.site-footer{background:var(--footer);color:#b8c6d4;display:flex;gap:22px;padding:16px 38px 0;height:115px}
.site-footer h4{font-size:7px;font-weight:700;color:var(--white);text-transform:uppercase;margin-bottom:6px}
.site-footer ul{list-style:none;font-size:6.3px;line-height:1.6}
.site-footer p{font-size:6.3px;line-height:1.6}
.chat{margin-top:6px;width:92px;height:34px;background:var(--blue-bright);color:var(--white);padding:5px 8px;font-size:6.5px;line-height:1.3}
.chat strong{display:block;font-size:8px}
.social-col{margin-left:auto}
.social{display:flex;gap:4px}
.social span{width:18px;height:18px;background:var(--blue)}
.bottom-bar{background:var(--bottom);color:#7f91a3;font-size:6px;padding:0 38px;height:23px;display:flex;align-items:center}
</style>
</head>
<body>

<header class="site-header">
  <div class="brand"><span class="brand-mark"></span>Hollow Pine Computers</div>
  <nav class="main-nav">
    <a href="#">HOME</a><a href="#">PRODUCTS</a><a href="#">SERVICES</a><a href="#">COMPANY</a><a class="login" href="#">USER LOGIN</a>
  </nav>
</header>

<section class="hero" role="img" aria-label="Glowing blue digital technology tunnel background">
  <h1>MAKING YOUR TECHNOLOGY</h1>
  <p>WORK FOR YOU</p>
</section>

<section class="welcome">
  <div class="welcome-text">
    <h2>Welcome to Hollow Pine Computers</h2>
    <div class="rule"></div>
    <p>Hollow Pine Computers is a locally owned and operated full service computer solutions center.</p>
    <p>Our goal is to build a relationship with our clients, communicate clearly, and find timely, cost effective solutions to your needs.</p>
    <p>From in-shop repair for personal computer systems to completely managed network contracts for our commercial clients, we deliver the service that best suits your unique requirements.</p>
  </div>
  <div class="storefront" role="img" aria-label="Photo of the computer shop storefront with red awning"></div>
</section>

<section class="services">
  <div class="service">
    <svg viewBox="0 0 24 24" fill="none" stroke="#1f6fb5" stroke-width="1.6"><rect x="5" y="3" width="14" height="18" rx="1"/><line x1="8" y1="8" x2="16" y2="8"/><line x1="8" y1="12" x2="16" y2="12"/><circle cx="12" cy="17" r="1"/></svg>
    <h3>Commercial<br>IT Support</h3>
    <p>Lorem ipsum dolor sit amet, consectetur adipiscing elit.</p><a class="more" href="#">Read More &gt;</a>
  </div>
  <div class="service">
    <svg viewBox="0 0 24 24" fill="none" stroke="#1f6fb5" stroke-width="1.6"><rect x="4" y="9" width="16" height="12" rx="1"/><path d="M6 9V5h12v4"/><line x1="8" y1="13" x2="10" y2="13"/><line x1="12" y1="13" x2="14" y2="13"/><line x1="8" y1="17" x2="10" y2="17"/><line x1="12" y1="17" x2="14" y2="17"/></svg>
    <h3>Commercial<br>Phone Systems</h3>
    <p>Lorem ipsum dolor sit amet, consectetur adipiscing elit.</p><a class="more" href="#">Read More &gt;</a>
  </div>
  <div class="service">
    <svg viewBox="0 0 24 24" fill="none" stroke="#1f6fb5" stroke-width="1.6"><rect x="6" y="3" width="12" height="18" rx="1"/><rect x="8" y="5" width="8" height="5"/><line x1="9" y1="13" x2="15" y2="13"/><line x1="9" y1="16" x2="15" y2="16"/></svg>
    <h3>Point of<br>Sale Systems</h3>
    <p>Lorem ipsum dolor sit amet, consectetur adipiscing elit.</p><a class="more" href="#">Read More &gt;</a>
  </div>
  <div class="service">
    <svg viewBox="0 0 24 24" fill="none" stroke="#1f6fb5" stroke-width="1.6"><rect x="3" y="4" width="18" height="12" rx="1"/><line x1="12" y1="16" x2="12" y2="20"/><line x1="8" y1="20" x2="16" y2="20"/></svg>
    <h3>Web<br>Design</h3>
    <p>Lorem ipsum dolor sit amet, consectetur adipiscing elit.</p><a class="more" href="#">Read More &gt;</a>
  </div>
  <div class="service">
    <svg viewBox="0 0 24 24" fill="none" stroke="#1f6fb5" stroke-width="1.6"><path d="M4 11l8-7 8 7"/><path d="M6 10v10h12V10"/><rect x="10" y="14" width="4" height="6"/></svg>
    <h3>Hollow Pine<br>Computers</h3>
    <p>Lorem ipsum dolor sit amet, consectetur adipiscing elit.</p><a class="more" href="#">Read More &gt;</a>
  </div>
</section>

<div class="partners-block">
  <div class="partners">
    <section>
      <h2>Solutions for your tech needs</h2>
      <div class="rule"></div>
      <div class="logo-row">
        <span class="partner-name">Remvia</span>
        <span class="partner-name">Linkdesk</span>
        <span class="partner-name">Helmora</span>
      </div>
    </section>
    <section>
      <h2>Our Partner</h2>
      <div class="rule"></div>
      <div class="logo-row">
        <span class="partner-sq"></span>
        <span class="partner-name">Tillmora</span>
        <span class="partner-name">Voxtrell</span>
      </div>
    </section>
  </div>
  <div class="certs"><span class="cert"></span><span class="cert"></span><span class="cert"></span></div>
</div>

<section class="stories">
  <section>
    <div class="badge"><svg width="10" height="10" viewBox="0 0 10 10" fill="none" stroke="#4fb4e8" stroke-width="1.2"><path d="M2 8l1-3 4-4 2 2-4 4z"/></svg></div>
    <h2>From our blog</h2>
    <div class="rule"></div>
    <h3>Lorem ipsum dolor sit amet, consectetur adipiscing elit</h3>
    <div class="meta">by ADMIN, 14/06/2015</div>
    <p>Lorem ipsum dolor sit amet, consectetur adipiscing elit, sed do eiusmod tempor incididunt ut labore et dolore magna aliqua. Ut enim ad minim veniam, quis nostrud exercitation ullamco laboris nisi ut aliquip ex ea commodo consequat.</p>
    <a class="more" href="#">Read more &gt;</a>
  </section>
  <section>
    <div class="badge"><svg width="10" height="10" viewBox="0 0 10 10" fill="#4fb4e8"><rect x="1" y="2" width="3" height="3"/><rect x="6" y="2" width="3" height="3"/><path d="M1 5h3l-2 3z"/><path d="M6 5h3l-2 3z"/></svg></div>
    <h2>Here's what people around the world are saying</h2>
    <div class="rule"></div>
    <p class="quote">"Lorem ipsum dolor sit amet, consectetur adipiscing elit, sed do eiusmod tempor incididunt ut labore et dolore magna aliqua. Ut enim ad minim veniam, quis nostrud exercitation ullamco laboris nisi ut aliquip ex ea commodo consequat."</p>
    <a class="more" href="#">View our Testimonials &gt;</a>
    <div class="author">Dale Morrow</div>
  </section>
</section>

<section class="contact-strip">
  <h2>Have<br>questions?</h2>
  <div class="cta"><span class="cta-icon"><svg width="9" height="9" viewBox="0 0 10 10" fill="#fff"><path d="M2 1l2 0 1 2-1 1a6 6 0 0 0 2 2l1-1 2 1v2a1 1 0 0 1-1 1A8 8 0 0 1 1 2a1 1 0 0 1 1-1z"/></svg></span><span>Call us<strong>555-013-2917</strong></span></div>
  <div class="cta"><span class="cta-icon"><svg width="9" height="9" viewBox="0 0 10 10" fill="none" stroke="#fff"><rect x="1" y="2.5" width="8" height="5.5"/><path d="M1 2.5l4 3 4-3"/></svg></span><span>Send us<strong>an email</strong></span></div>
  <div class="cta"><span class="cta-icon"><svg width="9" height="9" viewBox="0 0 10 10" fill="#fff"><path d="M5 1a3 3 0 0 1 3 3c0 2-3 5-3 5S2 6 2 4a3 3 0 0 1 3-3z"/></svg></span><span>Find a<strong>local office</strong></span></div>
  <div class="cta"><span class="cta-icon"><svg width="9" height="9" viewBox="0 0 10 10" fill="none" stroke="#fff"><path d="M3 4a2 2 0 1 1 3 1.6c-1 .6-1 1-1 1.9"/><circle cx="5" cy="9" r=".4" fill="#fff"/></svg></span><span>Read the<strong>FAQs</strong></span></div>
</section>

<footer class="site-footer">
  <div><h4>Quick links</h4><ul><li>Home</li><li>Products</li><li>Services</li><li>Company</li></ul></div>
  <div><h4>Office hours</h4><p>Monday-Friday: 8am to 6pm<br>Saturday: 9am to 1pm<br>Sunday: Closed</p></div>
  <div><h4>Contact us</h4><p>412 N. Cedar Ave.<br>Suite 3<br>Fairhaven, IN 47021</p></div>
  <div><div class="chat"><strong>LIVE CHAT</strong>Chat with us now</div></div>
  <div class="social-col"><h4>Social media</h4><div class="social"><span></span><span></span><span></span><span></span></div></div>
</footer>
<div class="bottom-bar">© 2015 Hollow Pine Computers. All Rights Reserved. | Terms and Conditions | Privacy Policy | Terms of Use</div>

</body>
</html>
```